Need a Brochure Design

We need a brochure designed (A4 two sides or A3 foldable which is equal to 2 x A4 = total of four pages )

Brief and Logo attached.

```html
<!DOCTYPE html>
<html lang="en">
<head>
<meta charset="utf-8">
<title>Nest Styling Co – Brochure</title>
<link href="https://fonts.googleapis.com/css2?family=Bebas+Neue&family=Josefin+Sans:wght@400;600;700&family=Montserrat:wght@300;400;500;600;700&display=swap" rel="stylesheet">
<style>
:root{
  --stage:#7b7b7b;
  --orange:#f58a46;
  --orange-deep:#f0782e;
  --peach:#fde3d2;
  --peach-soft:#fff1e7;
  --charcoal:#2b2f33;
  --ink:#3a3a3a;
  --white:#ffffff;
}
*{margin:0;padding:0;box-sizing:border-box}
html,body{width:1200px;height:861px;overflow:hidden}
body{background:var(--stage);font-family:"Montserrat",sans-serif;color:var(--ink);position:relative}
.page{position:absolute;top:53px;width:530px;height:746px;background:var(--white);overflow:hidden}
.page--front{left:59px}
.page--back{left:623px;width:529px}
.abs{position:absolute}
.photo{position:absolute}

/* front */
.hero-photo{left:0;top:0;width:530px;height:220px;background:linear-gradient(160deg,#e9e6e1 0%,#cfc5b7 45%,#9a7652 75%,#d9d6d1 100%)}
.brand-panel{left:45px;top:0;width:123px;height:114px;background:var(--white);border-radius:0 0 62px 62px;display:flex;align-items:center;justify-content:center}
.brand-name{font-family:"Montserrat",sans-serif;font-weight:500;font-size:12px;color:var(--charcoal);letter-spacing:.5px;text-align:center;line-height:1.2}
.offer-tag{left:317px;top:0;width:213px;height:26px;background:var(--charcoal);clip-path:polygon(6% 0,100% 0,100% 100%,14% 100%);color:var(--white);font-family:"Bebas Neue",sans-serif;font-size:19px;line-height:28px;padding-left:27px;letter-spacing:.3px}
.tagline-band{left:0;top:219px;width:530px;height:27px;background:var(--orange);color:var(--white);font-family:"Bebas Neue",sans-serif;font-size:19px;line-height:29px;padding-left:35px;letter-spacing:.4px}
.intro-band{left:0;top:246px;width:530px;height:148px;background:var(--charcoal)}
.team-photo{left:298px;top:215px;width:208px;height:208px;border-radius:50%;border:4px solid var(--white);background:radial-gradient(circle at 50% 60%,#f2efeb 0%,#d8d4cf 45%,#8e7f72 80%,#6a5646 100%)}
.owner-photo{left:33px;top:263px;width:62px;height:62px;border-radius:50%;background:radial-gradient(circle at 50% 45%,#d9cfc6 0%,#a99a8e 60%,#e9e4df 100%)}
.greeting{left:101px;top:266px;font-size:12.5px;color:var(--orange);font-weight:400}
.intro-text{color:#e9e9e9;font-size:7.7px;line-height:10.6px}
.intro-text--lead{left:101px;top:284px;width:192px;text-align:justify}
.intro-text--body{left:37px;top:330px;width:256px}
.section-title{font-size:10.6px;font-weight:400;color:#505050;text-transform:uppercase;letter-spacing:.1px}
.body-copy{font-size:7.9px;line-height:10.6px;color:#444}
.impressions-title{left:35px;top:406px}
.impressions-copy{left:35px;top:430px;width:472px}
.impressions-copy p{margin-bottom:4.5px}
.connected-title{left:35px;top:511px}
.connected-copy{left:37px;top:532px;width:180px;text-align:justify}
.why-title{left:270px;top:511px}
.why-list{left:270px;top:531px;list-style:none}
.why-list li{font-size:7.9px;line-height:12.3px;color:#444;display:flex;align-items:center;gap:3px}
.why-list svg{width:9px;height:9px}
.wash{background:radial-gradient(ellipse at 30% 60%,var(--peach) 0%,var(--peach-soft) 55%,rgba(255,255,255,0) 80%)}
.front-wash{left:0;top:590px;width:530px;height:150px;opacity:.9}
.referral-title{left:33px;top:619px}
.referral-big{left:33px;top:636px;font-size:38px;font-weight:400;color:#4a4a4a;letter-spacing:.5px;line-height:40px}
.referral-voucher{left:34px;top:674px;font-family:"Bebas Neue",sans-serif;font-size:26px;color:var(--orange-deep);line-height:26px}
.referral-note{left:33px;top:698px;font-family:"Bebas Neue",sans-serif;font-size:15px;color:#4a4a4a;line-height:16px}
.contact-title{left:264px;top:613px;font-size:9.4px;line-height:13.5px;white-space:nowrap;letter-spacing:0}
.contact-phone{left:263px;top:642px;display:flex;align-items:center;gap:4px;font-family:"Josefin Sans",sans-serif;font-weight:700;font-size:19px;line-height:20px;color:#3a3a3a}
.contact-phone svg{width:13px;height:13px}
.contact-email{left:264px;top:663px;font-size:9.6px;color:#555}
.site-title{left:263px;top:682px}
.contact-site{left:263px;top:698px;display:flex;align-items:center;gap:4px;font-family:"Josefin Sans",sans-serif;font-weight:700;font-size:13px;color:#3a3a3a}
.contact-site svg{width:13px;height:13px}
.front-foot{left:0;top:733px;width:530px;height:13px;background:var(--orange)}

/* back */
.headline-band{left:0;top:0;width:529px;height:85px;background:var(--orange)}
.headline{left:0;top:33px;width:529px;text-align:center;color:var(--charcoal);line-height:14.6px}
.headline .l1{font-size:14px;font-weight:400}
.headline .l2{font-size:14.5px;font-weight:700}
.back-wash{left:0;top:80px;width:529px;height:200px;background:radial-gradient(ellipse at 50% 40%,var(--peach) 0%,var(--peach-soft) 50%,rgba(255,255,255,0) 80%)}
.price-table{left:35px;top:74px;width:456px;border-collapse:collapse;font-family:"Josefin Sans",sans-serif}
.price-table th{background:var(--charcoal);color:var(--orange);height:26px;font-weight:700;font-size:7.8px;text-align:center}
.price-table th.plan{font-family:"Bebas Neue",sans-serif;font-size:15.5px;font-weight:400;text-align:left;padding-left:38px;letter-spacing:.3px}
.price-table td{border:1px solid var(--charcoal);height:40px;text-align:center;vertical-align:middle;background:rgba(255,255,255,.35)}
.price-table col.c1{width:205px}.price-table col.c2{width:92px}.price-table col.c3{width:96px}.price-table col.c4{width:63px}
.plan-name{font-size:14.5px;font-weight:600;color:var(--charcoal);line-height:14px}
.plan-sub{font-size:7.8px;font-weight:700;color:var(--charcoal)}
.price-sale{font-size:12px;font-weight:700;color:var(--orange-deep)}
.price-was{font-size:12px;color:#555;text-decoration:line-through}
.sale-flag{font-size:10px;color:var(--orange);font-family:"Montserrat",sans-serif}
.table-note{left:52px;top:262px;font-size:7.6px;color:var(--charcoal);background:var(--white);padding:0 2px}
.table-under{left:35px;top:267px;width:394px;height:1px;background:var(--charcoal)}
.gallery-living{left:34px;top:291px;width:299px;height:110px;background:linear-gradient(180deg,#eeeeec 0%,#d9d7d3 55%,#b5aea4 100%)}
.gallery-lounge{left:34px;top:406px;width:146px;height:106px;background:linear-gradient(180deg,#e6e2dd 0%,#c5c1bd 50%,#2f3338 100%)}
.gallery-bedroom{left:187px;top:406px;width:146px;height:106px;background:linear-gradient(180deg,#eceff2 0%,#d9dde2 50%,#e4c2c0 100%)}
.gallery-cushions{left:340px;top:290px;width:151px;height:223px;background:linear-gradient(160deg,#efeeec 0%,#cfc9c3 50%,#6d7f96 80%,#c9c9cc 100%)}
.benefits{left:33px;top:533px;list-style:none}
.benefits li{display:flex;align-items:center;gap:7px;font-size:9.8px;line-height:14px;color:#4a4a4a}
.benefits svg{width:9px;height:9px}
.back-brand-wash{left:310px;top:560px;width:190px;height:140px;background:radial-gradient(ellipse at 55% 50%,var(--peach) 0%,var(--peach-soft) 55%,rgba(255,255,255,0) 78%)}
.back-brand{left:330px;top:612px;width:160px;text-align:center;font-size:17px;font-weight:500;color:var(--charcoal);letter-spacing:.8px}
.back-contact-wash{left:0;top:620px;width:350px;height:90px;background:radial-gradient(ellipse at 40% 60%,var(--peach-soft) 0%,rgba(255,255,255,0) 75%)}
.back-contact-title{left:32px;top:637px;font-size:13.4px;color:var(--orange);font-weight:300;letter-spacing:.2px}
.back-phone{left:32px;top:653px;display:flex;align-items:center;gap:3px;font-family:"Josefin Sans",sans-serif;font-weight:700;font-size:23px;color:#2f2f2f}
.back-phone svg{width:16px;height:16px}
.back-email{left:32px;top:676px;font-size:8.6px;color:#555;letter-spacing:.2px}
.social-dots{left:224px;top:670px;display:flex;gap:3px}
.social-dots span{width:13px;height:13px;border-radius:50%;background:var(--orange)}
.back-foot{left:0;top:709px;width:529px;height:37px;background:var(--charcoal);color:var(--white);text-align:center;font-size:12.4px;line-height:37px;letter-spacing:2px}
.back-foot b{color:var(--orange);font-weight:600}
</style>
</head>
<body>

<section class="page page--front">
  <div class="photo hero-photo" role="img" aria-label="Styled open-plan dining room and kitchen with timber table"></div>
  <div class="abs brand-panel"><div class="brand-name">Nest<br>Styling Co</div></div>
  <div class="abs offer-tag">10 Weeks Free Rental</div>
  <div class="abs tagline-band">Flexible &amp; Affordable Property Styling</div>
  <div class="abs intro-band"></div>
  <div class="photo owner-photo" role="img" aria-label="Portrait of the owner"></div>
  <div class="abs greeting">HEY THERE,</div>
  <p class="abs intro-text intro-text--lead">I'm Mara, Owner and Creative Director of Nest Styling Co. Please let me introduce you to our amazingly creative property styling team!</p>
  <p class="abs intro-text intro-text--body">We are a friendly bunch who are passionate about home staging. We've been property staging apartments, townhouses, and stand-alone homes since 2009. An all-female powerhouse, we combine our experience in art, interior design, retail, and business to offer professional home styling throughout Melbourne.</p>
  <div class="photo team-photo" role="img" aria-label="Group photo of the styling team"></div>

  <h2 class="abs section-title impressions-title">Because First Impressions Count</h2>
  <div class="abs body-copy impressions-copy">
    <p>A gorgeous looking home sells faster and fetches a higher price.</p>
    <p>At NestStylingCo, we help our property clients create a lasting impression with minimal spend. Our property vendors are usually looking for home-staging on a tight budget. They come to us searching for creative transformations to help them sell well. Thoughtfully positioned furniture and on-trend interior décor can make all the difference!</p>
    <p>Our property styling service includes a free consultation, longer rental periods, &amp; installation &amp; removal.</p>
  </div>

  <h2 class="abs section-title connected-title">We're Well-Connected</h2>
  <p class="abs body-copy connected-copy">We have a steady flow of clients who have not yet secured their Real Estate Agents, so we'd be happy to share the love. We believe in last relationships, and we work with reputable agents across Melbourne.</p>

  <h2 class="abs section-title why-title">Why Choose Nest Styling Co?</h2>
  <ul class="abs why-list">
    <li><svg viewBox="0 0 10 10"><path d="M8.5 3.2A4 4 0 1 1 6.8 1.4" fill="none" stroke="#f58a46" stroke-width="1.2"/><path d="M3 5l2 2 4-5" fill="none" stroke="#f58a46" stroke-width="1.3"/></svg>Experienced, enthusiastic property stylists</li>
    <li><svg viewBox="0 0 10 10"><path d="M8.5 3.2A4 4 0 1 1 6.8 1.4" fill="none" stroke="#f58a46" stroke-width="1.2"/><path d="M3 5l2 2 4-5" fill="none" stroke="#f58a46" stroke-width="1.3"/></svg>Work with low client budgets</li>
    <li><svg viewBox="0 0 10 10"><path d="M8.5 3.2A4 4 0 1 1 6.8 1.4" fill="none" stroke="#f58a46" stroke-width="1.2"/><path d="M3 5l2 2 4-5" fill="none" stroke="#f58a46" stroke-width="1.3"/></svg>Fast turnaround to a tight deadline</li>
    <li><svg viewBox="0 0 10 10"><path d="M8.5 3.2A4 4 0 1 1 6.8 1.4" fill="none" stroke="#f58a46" stroke-width="1.2"/><path d="M3 5l2 2 4-5" fill="none" stroke="#f58a46" stroke-width="1.3"/></svg>Flexible rental terms (4/6/8 weeks)</li>
    <li><svg viewBox="0 0 10 10"><path d="M8.5 3.2A4 4 0 1 1 6.8 1.4" fill="none" stroke="#f58a46" stroke-width="1.2"/><path d="M3 5l2 2 4-5" fill="none" stroke="#f58a46" stroke-width="1.3"/></svg>Happy to recommend potential customers</li>
  </ul>

  <div class="abs wash front-wash"></div>
  <h2 class="abs section-title referral-title">We Reward Referrals!</h2>
  <div class="abs referral-big">WE OFFER</div>
  <div class="abs referral-voucher">A $200 Gift Voucher</div>
  <div class="abs referral-note">For Every Successful Referral To Us!</div>

  <h2 class="abs section-title contact-title">We'd love to hear from you, so please<br>contact us by telephone, text, or email:</h2>
  <div class="abs contact-phone"><svg viewBox="0 0 16 16"><path d="M4 1.5l2.3 3-1.4 1.6a9 9 0 0 0 5 5l1.6-1.4 3 2.3-1.6 2.3C7.5 14 2 8.5 1.7 3.1z" fill="none" stroke="#f58a46" stroke-width="1.3"/></svg>0400 123 456</div>
  <div class="abs contact-email">hello@neststylingco.com.au</div>
  <h2 class="abs section-title site-title">Please also visit our website</h2>
  <div class="abs contact-site"><svg viewBox="0 0 16 16"><circle cx="8" cy="8" r="6.5" fill="none" stroke="#f58a46" stroke-width="1.2"/><ellipse cx="8" cy="8" rx="3" ry="6.5" fill="none" stroke="#f58a46" stroke-width="1"/><path d="M1.5 8h13M2.5 5h11M2.5 11h11" stroke="#f58a46" stroke-width="1"/></svg>neststylingco.com.au</div>
  <div class="abs front-foot"></div>
</section>

<section class="page page--back">
  <div class="abs headline-band"></div>
  <div class="abs back-wash"></div>
  <div class="abs headline">
    <div class="l1">WE AVERAGE OVER 185 PROPERTY STYLING PROJECTS PER YEAR</div>
    <div class="l2">WITH A LARGE PROPORTION SELLING IN LESS THAN 30 DAYS!</div>
  </div>

  <table class="abs price-table">
    <colgroup><col class="c1"><col class="c2"><col class="c3"><col class="c4"></colgroup>
    <thead><tr><th class="plan">Plans &amp; Prices</th><th>SALE PRICE</th><th>ORIGINAL PRICE</th><th>SALE</th></tr></thead>
    <tbody>
      <tr><td><div class="plan-name">1 Bedroom Property</div><div class="plan-sub">Full Styling &nbsp;+&nbsp; 10 Weeks Free Hire*</div></td><td class="price-sale">1,897.00</td><td class="price-was">2,750.00</td><td class="sale-flag">SALE</td></tr>
      <tr><td><div class="plan-name">2 Bedroom Property</div><div class="plan-sub">Full Styling &nbsp;+&nbsp; 10 Weeks Free Hire*</div></td><td class="price-sale">2,397.00</td><td class="price-was">3,250.00</td><td class="sale-flag">SALE</td></tr>
      <tr><td><div class="plan-name">3 Bedroom Property</div><div class="plan-sub">Full Styling &nbsp;+&nbsp; 10 Weeks Free Hire*</div></td><td class="price-sale">2,697.00</td><td class="price-was">4,470.00</td><td class="sale-flag">SALE</td></tr>
      <tr><td><div class="plan-name">4 Bedroom Property</div><div class="plan-sub">Full Styling &nbsp;+&nbsp; 10 Weeks Free Hire*</div></td><td class="price-sale">2,997.00</td><td class="price-was">5,485.00</td><td class="sale-flag">SALE</td></tr>
    </tbody>
  </table>
  <div class="abs table-under"></div>
  <div class="abs table-note">*4 Weeks Free Hire + 2 or 4 Weeks Free Extension (if property not sold within 4 weeks)</div>

  <div class="photo gallery-living" role="img" aria-label="Bright styled living room opening to kitchen and dining"></div>
  <div class="photo gallery-lounge" role="img" aria-label="Styled lounge with grey sofas and dark rug"></div>
  <div class="photo gallery-bedroom" role="img" aria-label="Stylists making up a bed with pink throw"></div>
  <div class="photo gallery-cushions" role="img" aria-label="Stylist arranging cushions on a sofa"></div>

  <ul class="abs benefits">
    <li><svg viewBox="0 0 10 10"><circle cx="5" cy="5" r="5" fill="#f58a46"/><path d="M2.6 5.1l1.7 1.6 3.2-3.4" fill="none" stroke="#fff" stroke-width="1.3"/></svg>Helping your property reach its highest potential without busting the budget.</li>
    <li><svg viewBox="0 0 10 10"><circle cx="5" cy="5" r="5" fill="#f58a46"/><path d="M2.6 5.1l1.7 1.6 3.2-3.4" fill="none" stroke="#fff" stroke-width="1.3"/></svg>Achieving a record number of viewings &amp; the highest possible sale price.</li>
    <li><svg viewBox="0 0 10 10"><circle cx="5" cy="5" r="5" fill="#f58a46"/><path d="M2.6 5.1l1.7 1.6 3.2-3.4" fill="none" stroke="#fff" stroke-width="1.3"/></svg>Installation, interior design &amp; decoration, &amp; removal included.</li>
    <li><svg viewBox="0 0 10 10"><circle cx="5" cy="5" r="5" fill="#f58a46"/><path d="M2.6 5.1l1.7 1.6 3.2-3.4" fill="none" stroke="#fff" stroke-width="1.3"/></svg>Pre-sale home preparation to post-sale removal.</li>
    <li><svg viewBox="0 0 10 10"><circle cx="5" cy="5" r="5" fill="#f58a46"/><path d="M2.6 5.1l1.7 1.6 3.2-3.4" fill="none" stroke="#fff" stroke-width="1.3"/></svg>Free consultation &amp; longer rental periods.</li>
    <li><svg viewBox="0 0 10 10"><circle cx="5" cy="5" r="5" fill="#f58a46"/><path d="M2.6 5.1l1.7 1.6 3.2-3.4" fill="none" stroke="#fff" stroke-width="1.3"/></svg>A small investment for such a large transformation!</li>
  </ul>

  <div class="abs back-brand-wash"></div>
  <div class="abs back-brand">Nest Styling Co</div>

  <div class="abs back-contact-wash"></div>
  <div class="abs back-contact-title">PLEASE CONTACT US ON</div>
  <div class="abs back-phone"><svg viewBox="0 0 16 16"><path d="M4 1.5l2.3 3-1.4 1.6a9 9 0 0 0 5 5l1.6-1.4 3 2.3-1.6 2.3C7.5 14 2 8.5 1.7 3.1z" fill="none" stroke="#2f2f2f" stroke-width="1.3"/></svg>0400 123 456</div>
  <div class="abs back-email">HELLO@NESTSTYLINGCO.COM.AU</div>
  <div class="abs social-dots"><span></span><span></span><span></span></div>

  <div class="abs back-foot">www.<b>neststylingco</b>.com.au</div>
</section>

</body>
</html>
```